1 Page Bio, describing our Mission to buy multifamily properties in Colorado Springs.

I am uploading a sample of an associate who is doing a similar thing in Tampa Florida. I will also upload an attempt by my assistant to make the flyer and I will upload 3 pictures to use, along with another document that has text to add. I want to be able to edit the document pretty easily inside a google doc. thanks, I want it to look clean and professional.

```html
<!DOCTYPE html>
<html lang="en">
<head>
<meta charset="UTF-8">
<title>Biography – Multifamily Mission</title>
<link href="https://fonts.googleapis.com/css2?family=Montserrat:wght@600;700;800&family=Open+Sans:wght@400;600&display=swap" rel="stylesheet">
<style>
  :root {
    --navy: #1d3557;
    --navy-deep: #16294a;
    --blue: #2d6aa8;
    --blue-light: #dfe9f3;
    --card-bg: #f4f6f8;
    --card-line: #d3d9df;
    --text: #2b2f33;
    --muted: #9aa3ab;
    --white: #ffffff;
  }
  * { box-sizing: border-box; margin: 0; padding: 0; }
  html, body { width: 849px; height: 1200px; overflow: hidden; background: var(--white); }
  body { font-family: "Open Sans", Arial, sans-serif; color: var(--text); position: relative; }

  .intro {
    position: absolute; left: 0; top: 0; width: 849px; height: 252px;
    background: linear-gradient(135deg, var(--navy) 0%, var(--navy-deep) 100%);
    color: var(--white); padding: 26px 40px;
  }
  .intro h2 { font-family: "Montserrat", Arial, sans-serif; font-weight: 800; font-size: 20px; letter-spacing: .5px; margin-bottom: 4px; }
  .intro p { font-size: 16px; margin-bottom: 18px; line-height: 1.35; }

  .market { position: absolute; top: 268px; left: 15px; width: 819px; height: 172px; display: flex; }
  .market-photo { width: 300px; height: 172px; background: linear-gradient(160deg, #7a8f6a 0%, #9aa88c 45%, #c9ccc4 100%); }
  .market-tab {
    width: 46px; height: 172px; background: var(--navy); color: var(--white);
    display: flex; align-items: center; justify-content: center;
  }
  .market-tab span {
    writing-mode: vertical-rl; transform: rotate(180deg);
    font-family: "Montserrat", Arial, sans-serif; font-weight: 800; font-size: 19px; letter-spacing: 1px;
  }
  .market-info { padding: 12px 0 0 20px; }
  .market-info h3 { font-family: "Montserrat", Arial, sans-serif; font-weight: 800; font-size: 16px; margin-bottom: 8px; }
  .market-info li { font-size: 15.5px; line-height: 1.45; list-style: none; position: relative; padding-left: 18px; }
  .market-info li::before { content: ""; position: absolute; left: 2px; top: 10px; width: 6px; height: 6px; background: var(--text); border-radius: 50%; }

  .target { position: absolute; top: 458px; left: 15px; width: 819px; }
  .target h2 { font-family: "Montserrat", Arial, sans-serif; font-weight: 800; font-size: 20px; }
  .target p { font-size: 16px; margin-top: 2px; }

  .team-band {
    position: absolute; top: 522px; left: 15px; width: 819px; height: 44px;
    background: var(--navy); color: var(--white); text-align: center;
    font-family: "Montserrat", Arial, sans-serif; font-weight: 800; font-size: 21px; line-height: 44px; letter-spacing: .5px;
  }

  .principal {
    position: absolute; top: 578px; width: 402px; height: 532px;
    background: var(--card-bg); border: 1px solid var(--card-line);
    border-bottom: 8px solid var(--blue); padding: 0 22px;
  }
  .principal.first { left: 15px; }
  .principal.second { left: 432px; }
  .avatar {
    display: block; width: 150px; height: 150px; border-radius: 50%;
    margin: 26px auto 24px; background: linear-gradient(180deg, #e3e6e9, #c7ccd1);
    border: 4px solid var(--white); box-shadow: 0 0 0 1px var(--card-line);
  }
  .principal h3 { font-family: "Montserrat", Arial, sans-serif; font-weight: 800; font-size: 18px; margin-bottom: 8px; }
  .credentials { list-style: none; }
  .credentials li { font-size: 14.5px; line-height: 1.38; padding-left: 24px; position: relative; margin-bottom: 3px; }
  .credentials svg { position: absolute; left: 0; top: 3px; width: 15px; height: 15px; }

  .footer-rule { position: absolute; top: 1126px; left: 15px; width: 819px; height: 3px; background: var(--blue); }
  .footer-title {
    position: absolute; top: 1146px; left: 0; width: 849px; text-align: center;
    font-family: "Montserrat", Arial, sans-serif; font-weight: 800; font-size: 26px; letter-spacing: 1px; color: var(--text);
  }
</style>
</head>
<body>

<section class="intro">
  <h2>THE MISSION</h2>
  <p>To create a family business by purchasing Multifamily Residences, one at a time.</p>
  <h2>VALUES</h2>
  <p>To provide a white glove experience to all residences with a clean, safe, and fun environment.</p>
  <h2>THE PROCESS</h2>
  <p>Buy right, manage right, and finance right.</p>
</section>

<section class="market">
  <div class="market-photo" role="img" aria-label="Photo of the two principals standing together outdoors"></div>
  <div class="market-tab"><span>THE MARKET</span></div>
  <div class="market-info">
    <h3>COLORADO SPRINGS</h3>
    <ul>
      <li>Projected job growth of nearly 50%</li>
      <li>Below average unemployment rates.</li>
      <li>Above-average incomes.</li>
      <li>Solid economy, military, aerospace, electronics industry, and tourism.</li>
    </ul>
  </div>
</section>

<section class="target">
  <h2>THE TARGET</h2>
  <p>B and C class assets located in Colorado Springs or nearby submarkets.</p>
</section>

<div class="team-band">THE TEAM - PRINCIPALS</div>

<article class="principal first">
  <div class="avatar" role="img" aria-label="Portrait of Dean Halvorsen"></div>
  <h3>DEAN HALVORSEN</h3>
  <ul class="credentials">
    <li><svg viewBox="0 0 16 16"><rect x="1" y="1" width="14" height="14" fill="none" stroke="#2d6aa8" stroke-width="1.5"/><path d="M4 8l3 3 5-6" fill="none" stroke="#2d6aa8" stroke-width="1.8"/></svg>Licensed Colorado Real Estate Agent 18 years.</li>
    <li><svg viewBox="0 0 16 16"><rect x="1" y="1" width="14" height="14" fill="none" stroke="#2d6aa8" stroke-width="1.5"/><path d="M4 8l3 3 5-6" fill="none" stroke="#2d6aa8" stroke-width="1.8"/></svg>Broker-Owner of two Summit Realty Franchises 7 and 2 Years.</li>
    <li><svg viewBox="0 0 16 16"><rect x="1" y="1" width="14" height="14" fill="none" stroke="#2d6aa8" stroke-width="1.5"/><path d="M4 8l3 3 5-6" fill="none" stroke="#2d6aa8" stroke-width="1.8"/></svg>Real Estate investing for 5 years.</li>
    <li><svg viewBox="0 0 16 16"><rect x="1" y="1" width="14" height="14" fill="none" stroke="#2d6aa8" stroke-width="1.5"/><path d="M4 8l3 3 5-6" fill="none" stroke="#2d6aa8" stroke-width="1.8"/></svg>Member of Keystone Investors Academy.</li>
    <li><svg viewBox="0 0 16 16"><rect x="1" y="1" width="14" height="14" fill="none" stroke="#2d6aa8" stroke-width="1.5"/><path d="M4 8l3 3 5-6" fill="none" stroke="#2d6aa8" stroke-width="1.8"/></svg>Married 24 years to Joan, parenting 10 children together.</li>
    <li><svg viewBox="0 0 16 16"><rect x="1" y="1" width="14" height="14" fill="none" stroke="#2d6aa8" stroke-width="1.5"/><path d="M4 8l3 3 5-6" fill="none" stroke="#2d6aa8" stroke-width="1.8"/></svg>Appeared on Ben and Sam's Apartment Hour podcast Episode 43</li>
    <li><svg viewBox="0 0 16 16"><rect x="1" y="1" width="14" height="14" fill="none" stroke="#2d6aa8" stroke-width="1.5"/><path d="M4 8l3 3 5-6" fill="none" stroke="#2d6aa8" stroke-width="1.8"/></svg>$2M portfolio.</li>
  </ul>
</article>

<article class="principal second">
  <div class="avatar" role="img" aria-label="Portrait of Walt Halvorsen"></div>
  <h3>WALT HALVORSEN</h3>
  <ul class="credentials">
    <li><svg viewBox="0 0 16 16"><rect x="1" y="1" width="14" height="14" fill="none" stroke="#2d6aa8" stroke-width="1.5"/><path d="M4 8l3 3 5-6" fill="none" stroke="#2d6aa8" stroke-width="1.8"/></svg>Retired Electrical Engineer.</li>
    <li><svg viewBox="0 0 16 16"><rect x="1" y="1" width="14" height="14" fill="none" stroke="#2d6aa8" stroke-width="1.5"/><path d="M4 8l3 3 5-6" fill="none" stroke="#2d6aa8" stroke-width="1.8"/></svg>Active Real Estate Investor/Consultant.</li>
    <li><svg viewBox="0 0 16 16"><rect x="1" y="1" width="14" height="14" fill="none" stroke="#2d6aa8" stroke-width="1.5"/><path d="M4 8l3 3 5-6" fill="none" stroke="#2d6aa8" stroke-width="1.8"/></svg>Net worth over $4M</li>
    <li><svg viewBox="0 0 16 16"><rect x="1" y="1" width="14" height="14" fill="none" stroke="#2d6aa8" stroke-width="1.5"/><path d="M4 8l3 3 5-6" fill="none" stroke="#2d6aa8" stroke-width="1.8"/></svg>15 Grandchildren.</li>
  </ul>
</article>

<div class="footer-rule"></div>
<div class="footer-title">BIOGRAPHY</div>

</body>
</html>
```